Presentation Folder Design for Photographer

Professional photographer requires a presentation folder for marketing.
I specialise in architecture, corporate & commercial photography. The folder will be used to promote my architectural photography services to real estate, accomodation & architect clients.

I'm looking for a modern clean design that complements my logo with complimentary text & colours. I want to use some images in the design, probably a mix of images not just architectural. I need a print ready design in PDF as well as a PSD file that I can possibly edit / update images later on.

The folder will be a double sided design with no need for pockets included in the design. Overall dimensions are 430mm ( folded down the centre ) x 315mm with a 5mm trim & bleed.

The layout would be as follows :

Front cover - Logo + maybe some images or some other design work.

Inside front cover - Some text about my services.

ARCHITECTURE
Commercial Residential Real Estate Drone Floorpans Accommodation

CORPORATE
Studio Headshots Environmental Portraits Staff Photography

COMMERCIAL
Product Advertising Fashion Event Stock

Inside back cover - no text as a seperate price list will sit here.

Outside back cover - I was thinking of having a collage of images worked into
the design but open to the designers input as well.
I also have another logo with phone number & web address
I would like on the back cover - Will be included in the files
provided.

I have a black background & white background version of my logo I will include both for the design work. I'm trying to get away from an all black design so if using the black logo I don't want a completely black page design, just becomes to heavy.

I'm redoing my website soon so please base the folder design around my logo text & colours not my current website as it's very outdated.

Logo brand guide is as follows

Main Font Font: Reislust
Main Font Color: #fff
Slogan Font Font: Ubuntu Bold
Monogram Font Font: Venti Medium
Container Color: #fff

Please respect the copyright on the images provided and delete all content once the design has been completed.
Thanks.

```html
<!DOCTYPE html>
<html lang="en">
<head>
<meta charset="utf-8">
<title>Presentation Folder – Outer Spread</title>
<link rel="stylesheet" href="https://fonts.googleapis.com/css2?family=Josefin+Sans:wght@300;400&family=Ubuntu:wght@700&display=swap">
<style>
  :root {
    --page-bg: #e4e4e4;
    --paper: #fbfbfb;
    --ink: #2a2a2a;
    --gold-light: #f3e3a2;
    --gold: #d4b255;
    --gold-deep: #b8902e;
    --fold: #e2e2e2;
  }
  * { margin: 0; padding: 0; box-sizing: border-box; }
  html, body { width: 1200px; height: 900px; overflow: hidden; }
  body {
    background: var(--page-bg);
    font-family: "Josefin Sans", sans-serif;
    color: var(--ink);
    position: relative;
  }
  .folder-spread {
    position: absolute;
    left: 50px; top: 47px;
    width: 1100px; height: 806px;
    display: flex;
    background: var(--paper);
    box-shadow: 0 6px 24px rgba(0,0,0,0.12);
  }
  .cover {
    position: relative;
    width: 550px; height: 806px;
  }
  .cover + .cover { border-left: 1px solid var(--fold); }
  .cover-art { position: absolute; inset: 0; }
  .brand {
    position: absolute;
    top: 92px; left: 0; right: 0;
    display: flex; justify-content: center; align-items: center; gap: 12px;
  }
  .brand-mark {
    width: 34px; height: 34px;
    border: 2px solid var(--gold);
  }
  .brand-text { display: flex; flex-direction: column; }
  .brand-name {
    font-weight: 300;
    font-size: 22px;
    letter-spacing: 1px;
    text-transform: uppercase;
    color: var(--gold-deep);
  }
  .brand-slogan {
    font-family: "Ubuntu", sans-serif;
    font-weight: 700;
    font-size: 7px;
    letter-spacing: 1.2px;
    color: var(--ink);
    margin-top: 3px;
  }
  .photographer-credit {
    position: absolute;
    font-weight: 400;
    text-transform: uppercase;
    white-space: nowrap;
  }
  .photographer-credit--front {
    left: 0; right: 0;
    bottom: 86px;
    text-align: center;
    font-size: 13px;
    letter-spacing: 2.5px;
  }
  .photographer-credit--back {
    left: 42px;
    top: 403px;
    font-size: 17px;
    letter-spacing: 4px;
    transform: translate(-50%, -50%) rotate(-90deg);
  }
</style>
</head>
<body>
  <main class="folder-spread">
    <!-- Outside back cover -->
    <section class="cover cover--back">
      <svg class="cover-art" width="550" height="806" viewBox="0 0 550 806">
        <defs>
          <linearGradient id="goldBack" x1="0" y1="0" x2="0" y2="1">
            <stop offset="0" stop-color="var(--gold-light)"/>
            <stop offset="1" stop-color="var(--gold)"/>
          </linearGradient>
          <linearGradient id="interiorTone" x1="0" y1="0" x2="1" y2="1">
            <stop offset="0" stop-color="#c2ab9c"/>
            <stop offset="0.5" stop-color="#8c6c55"/>
            <stop offset="1" stop-color="#4d3e2f"/>
          </linearGradient>
          <linearGradient id="exteriorTone" x1="0" y1="0" x2="0" y2="1">
            <stop offset="0" stop-color="#2f5c7a"/>
            <stop offset="0.45" stop-color="#4a4d50"/>
            <stop offset="0.75" stop-color="#8a4a26"/>
            <stop offset="1" stop-color="#5d6a36"/>
          </linearGradient>
        </defs>
        <rect class="gold-band" x="72" y="60" width="10" height="340" fill="url(#goldBack)"/>
        <rect class="photo" x="96" y="60" width="414" height="320" fill="url(#interiorTone)" role="img" aria-label="Photo: modern living room interior with large windows"/>
        <rect class="photo" x="96" y="400" width="414" height="346" fill="url(#exteriorTone)" role="img" aria-label="Photo: dark-clad house and timber deck at dusk"/>
      </svg>
      <p class="photographer-credit photographer-credit--back">Photographer Martin Hale</p>
    </section>

    <!-- Front cover -->
    <section class="cover cover--front">
      <svg class="cover-art" width="550" height="806" viewBox="0 0 550 806">
        <defs>
          <linearGradient id="goldBand" x1="0" y1="0" x2="1" y2="0">
            <stop offset="0" stop-color="var(--gold)"/>
            <stop offset="0.2" stop-color="var(--gold-light)"/>
            <stop offset="0.45" stop-color="#ffffff"/>
            <stop offset="0.8" stop-color="var(--gold-light)"/>
            <stop offset="1" stop-color="var(--gold)"/>
          </linearGradient>
          <linearGradient id="bedroomTone" x1="0" y1="0" x2="0" y2="1">
            <stop offset="0" stop-color="#e9ded4"/>
            <stop offset="1" stop-color="#c2a48c"/>
          </linearGradient>
          <linearGradient id="fashionTone" x1="0" y1="0" x2="0" y2="1">
            <stop offset="0" stop-color="#8a7a62"/>
            <stop offset="1" stop-color="#2c2a28"/>
          </linearGradient>
          <linearGradient id="brickTone" x1="0" y1="0" x2="0" y2="1">
            <stop offset="0" stop-color="#a5492f"/>
            <stop offset="0.55" stop-color="#6f8a3e"/>
            <stop offset="1" stop-color="#4e6a2c"/>
          </linearGradient>
          <linearGradient id="skyTone" x1="0" y1="0" x2="0" y2="1">
            <stop offset="0" stop-color="#5a68a8"/>
            <stop offset="1" stop-color="#9a4a36"/>
          </linearGradient>
        </defs>
        <rect class="gold-band" x="30" y="200" width="490" height="420" fill="url(#goldBand)"/>
        <polygon class="photo" points="140,200 225,200 165,620 80,620" fill="url(#bedroomTone)" role="img" aria-label="Photo: bedroom with chandelier and framed pictures"/>
        <polygon class="photo" points="235,200 320,200 260,620 175,620" fill="url(#fashionTone)" role="img" aria-label="Photo: fashion shoot in a stone building"/>
        <polygon class="photo" points="330,200 415,200 355,620 270,620" fill="url(#brickTone)" role="img" aria-label="Photo: red brick church above a flowering garden"/>
        <polygon class="photo" points="425,200 510,200 450,620 365,620" fill="url(#skyTone)" role="img" aria-label="Photo: brick tower against a blue sky"/>
      </svg>
      <div class="brand">
        <span class="brand-mark"></span>
        <div class="brand-text">
          <span class="brand-name">Clear Frame Studio</span>
          <span class="brand-slogan">Architecture Corporate Commercial</span>
        </div>
      </div>
      <p class="photographer-credit photographer-credit--front">Photographer Martin Hale</p>
    </section>
  </main>
</body>
</html>
```